Stickers to put on my honeyglasses

Stickers for my honey glasses.
Only a single sticker on the front. Same should have a stripe on the top side which goes above the lid to show if the glass was opened.
Size of the main part should be 55mm high and max. 100 mm wide.
The stripe on the top should be 70mm long.
I added a Picture of another producer which uses the same glass as I do.
I should say: 'e Lendorf Glas Hunneg'. which means 'another glass of honey. 'Hunneg' should be mainly visible and therefore very large. 'e Lendorf Glas' should be less visible and therefore smaller above the 'Hunneg'
- It needs to contain the quantity : '500gr'
- It needs to contain my Name and address: 'Marc Lendorf, 38, rue Ferd Lusang, L-9241 Kiemerich' (This should be small and not to visible)
- It needs to conatin a validity Line: ´Am beschte virum:` (With enough space so I can add a date by hand)
- It needs to say: 'dréchen, kill andäischterstockéieren' (to store it dry cold and dark)

```html
<!DOCTYPE html>
<html lang="lb">
<head>
<meta charset="utf-8">
<title>Hunneg – Etikett 500gr</title>
<link rel="stylesheet" href="https://fonts.googleapis.com/css2?family=Cabin:wght@400&family=Lato:wght@400&display=swap">
<style>
  :root {
    --paper: #ffffff;
    --label-cream: #fdebb8;
    --comb-tone: #ead6a0;
    --honey-brown: #5d3a22;
    --cut-line: #1f1a17;
    --measure: #1f1f1f;
  }
  html, body {
    margin: 0;
    padding: 0;
    width: 867px;
    height: 1200px;
    overflow: hidden;
    background: var(--paper);
  }
  .sheet { display: block; width: 867px; height: 1200px; }
  .label-shape { fill: var(--label-cream); stroke: var(--cut-line); stroke-width: 1.4; }
  .measure-line { stroke: var(--measure); stroke-width: 1.4; fill: none; }
  .measure-head { fill: var(--measure); }
  .measure-text { font-family: "Cabin", sans-serif; font-size: 19px; fill: var(--measure); }
  .comb-area { fill: url(#combFade); }
  .bee-area { fill: var(--honey-brown); opacity: 0.18; }
  .subtitle { font-family: "Cabin", sans-serif; font-size: 31px; fill: var(--honey-brown); }
  .product-name { font-family: "Lato", sans-serif; font-weight: 400; font-size: 110px; fill: var(--honey-brown); }
  .pill { fill: var(--honey-brown); }
  .pill-text { font-family: "Cabin", sans-serif; fill: var(--label-cream); text-anchor: middle; }
  .quantity { font-size: 19px; }
  .storage { font-size: 16px; }
  .best-before { font-family: "Cabin", sans-serif; font-size: 17px; fill: var(--honey-brown); }
  .date-line { stroke: var(--honey-brown); stroke-width: 0.8; }
  .maker-address { font-family: "Cabin", sans-serif; font-size: 11px; fill: var(--honey-brown); text-anchor: middle; }
</style>
</head>
<body>
<svg class="sheet" viewBox="0 0 867 1200" xmlns="http://www.w3.org/2000/svg">
  <defs>
    <linearGradient id="combFade" x1="0" y1="0" x2="0" y2="1">
      <stop offset="0" stop-color="#ead6a0" stop-opacity="0.25"/>
      <stop offset="0.5" stop-color="#ead6a0" stop-opacity="0.7"/>
      <stop offset="1" stop-color="#ead6a0" stop-opacity="0.25"/>
    </linearGradient>
  </defs>

  <!-- label die-cut outline: seal strip + main body -->
  <path class="label-shape" d="M392 145 H508 V595 H747 A24 24 0 0 1 771 619 V923 A24 24 0 0 1 747 947 H152 A24 24 0 0 1 128 923 V619 A24 24 0 0 1 152 595 H392 Z"/>

  <!-- honeycomb decoration zones -->
  <rect class="comb-area" role="img" aria-label="Faint honeycomb pattern on the seal strip" x="394" y="150" width="112" height="135"/>
  <rect class="comb-area" role="img" aria-label="Faint honeycomb pattern on the seal strip" x="394" y="340" width="112" height="250"/>
  <rect class="comb-area" role="img" aria-label="Faint honeycomb pattern behind the product name" x="138" y="660" width="624" height="222" rx="10"/>

  <!-- bee illustrations -->
  <rect class="bee-area" role="img" aria-label="Two small flying bees with a dotted flight path" x="241" y="603" width="94" height="83" rx="30"/>
  <rect class="bee-area" role="img" aria-label="Large bee illustration" x="658" y="616" width="94" height="99" rx="36"/>

  <!-- text -->
  <text class="subtitle" x="343" y="667">e Lendorf Glas</text>
  <text class="product-name" x="238" y="764" textLength="425" lengthAdjust="spacingAndGlyphs">HUNNEG</text>

  <rect class="pill" x="407" y="788" width="88" height="25" rx="12.5"/>
  <text class="pill-text quantity" x="451" y="807">500gr</text>

  <text class="best-before" x="212" y="862">´Am beschte virum</text>
  <line class="date-line" x1="381" y1="863" x2="690" y2="863"/>

  <rect class="pill" x="299" y="886" width="303" height="29" rx="14.5"/>
  <text class="pill-text storage" x="450" y="906">dréchen, kill andäischterstockéieren</text>

  <text class="maker-address" x="450" y="936">Marc Lendorf, 38, rue Ferd Lusang,  L-9241 Kiemerich</text>

  <!-- size marks -->
  <g class="measure">
    <line class="measure-line" x1="369" y1="150" x2="369" y2="584"/>
    <path class="measure-head" d="M369 141 L362 156 L369 152 L376 156 Z"/>
    <path class="measure-head" d="M369 591 L362 576 L369 580 L376 576 Z"/>
    <text class="measure-text" transform="translate(348 367) rotate(-90)" text-anchor="middle">70 mm</text>

    <line class="measure-line" x1="101" y1="600" x2="101" y2="936"/>
    <path class="measure-head" d="M101 592 L94 607 L101 603 L108 607 Z"/>
    <path class="measure-head" d="M101 944 L94 929 L101 933 L108 929 Z"/>
    <text class="measure-text" transform="translate(87 768) rotate(-90)" text-anchor="middle">55mm</text>

    <line class="measure-line" x1="136" y1="966" x2="763" y2="966"/>
    <path class="measure-head" d="M128 966 L143 959 L139 966 L143 973 Z"/>
    <path class="measure-head" d="M771 966 L756 959 L760 966 L756 973 Z"/>
    <text class="measure-text" x="443" y="988" text-anchor="middle">100mm</text>
  </g>
</svg>
</body>
</html>
```